Website for Lucent Prose Advisory Group

Please design a website that initially contains four or five pages. This work is for a newly formed consulting company, Lucent Prose Advisory Group, that provides training and individual coaching to help business professionals and lawyers write more effectively and efficiently.

We work in a professional and conservative industry. The website should be simple, crisp, and clean.

I have attached a document that describes the four initial pages for the site: 1) a landing page, 2) a webpage that includes the pictures and bios of our two consultants, 3) a webpage that describes our services, and 4) a webpage that will contain a form that visitors can use to submit questions to us.

I also included the following files:
a. a powerpoint slide with our consultants' pictures and bios; and
b. our recently designed logo (jpg and png files).

Thank you!

```html
<!DOCTYPE html>
<html lang="en">
<head>
<meta charset="utf-8">
<title>Lucent Prose Advisory Group</title>
<link href="https://fonts.googleapis.com/css2?family=Ubuntu:wght@400;500;700&family=Open+Sans:wght@400;600;700&display=swap" rel="stylesheet">
<style>
:root{
  --red:#c9252f;
  --red-soft:#cc4a55;
  --ink:#151515;
  --dark:#1f1f22;
  --navy:#141a2c;
  --navy-2:#222a40;
  --teal:#3dbfd8;
  --grey-bg:#f2f2f2;
  --text:#333;
  --muted:#777;
  --white:#fff;
}
*{margin:0;padding:0;box-sizing:border-box}
html,body{width:1200px;height:5121px;overflow:hidden}
body{position:relative;font-family:"Open Sans",sans-serif;color:var(--text);background:var(--white)}
.abs{position:absolute}
h1,h2,h3,h4,.heading{font-family:"Ubuntu",sans-serif;font-weight:500}
.ph{position:absolute}
.label{font-family:"Ubuntu",sans-serif;color:var(--red);font-size:16px}
.btn{position:absolute;background:var(--red);color:#fff;font:700 11px "Open Sans",sans-serif;display:flex;align-items:center;justify-content:center;gap:14px;border-radius:3px;text-transform:uppercase}
.btn svg{width:16px;height:12px}

/* hero */
.hero{position:absolute;left:0;top:0;width:1200px;height:676px;overflow:hidden}
.hero-photo{left:0;top:0;width:1200px;height:676px;background:linear-gradient(100deg,#1c2632 0%,#3a4855 45%,#6f7c88 70%,#4a5663 100%)}
.hero-shade{left:0;top:0;width:760px;height:676px;background:linear-gradient(90deg,rgba(12,18,26,.75),rgba(12,18,26,0))}
.nav{left:378px;top:0;width:497px;height:50px;background:#fff;border-radius:0 0 28px 28px;display:flex;justify-content:center;align-items:center;gap:38px;font:600 10px "Open Sans",sans-serif;color:#333}
.nav .active{color:#000;font-weight:700}
.logo{font-family:"Ubuntu",sans-serif;font-weight:500;color:#fff;font-size:15px}
.phone{left:904px;top:18px;display:flex;gap:10px;align-items:center;color:#fff}
.phone small{display:block;font-size:7px}
.phone b{font-size:9px}
.hero h1{left:228px;top:205px;font-size:48px;line-height:60px;color:#fff}
.hero p{left:234px;top:342px;width:440px;font-size:12.5px;line-height:22px;color:#e8e8e8}
.social{left:48px;width:24px;height:24px;border:1px solid #cfd6dc;border-radius:50%}
.hero-rule{left:40px;top:0;width:1px;height:676px;background:rgba(255,255,255,.18)}

/* about */
.about h2{left:117px;top:842px;font-size:34px;line-height:46px;color:var(--ink)}
.about p{left:122px;top:940px;width:420px;font-size:12px;line-height:22px;color:var(--muted)}
.quote-line{left:122px;top:1023px;color:var(--red);font-size:17px}

/* services */
.services{left:0;top:1407px;width:1200px;height:699px;background:var(--grey-bg)}
.sec-title{position:absolute;left:0;width:1200px;text-align:center}
.sec-title .label{display:block}
.sec-title h2{font-size:34px;color:var(--ink);margin-top:10px}
.card-box{position:absolute;background:var(--ink);color:#fff;text-align:center;padding-top:34px}
.card-box h3{font-size:24px;line-height:33px}
.card-box p{font-size:12px;line-height:21px;margin:12px auto 0;width:210px;color:#ddd}
.card-box .go{width:32px;height:32px;margin:14px auto 0;border:2px solid #fff;border-radius:50%;display:flex;align-items:center;justify-content:center}

/* why */
.why-black{left:0;top:2178px;width:600px;height:494px;background:var(--ink)}
.why-red{left:600px;top:2146px;width:600px;height:560px;background:linear-gradient(135deg,#c83c48,#d35a64 60%,#c3414c)}
.why h2{left:117px;top:2305px;font-size:34px;line-height:46px;color:#fff}
.why p{left:122px;top:2416px;width:430px;font-size:12px;line-height:22px;color:#ddd}
.why-frame{left:558px;top:2235px;width:475px;height:388px;border:3px solid #fff}
.tab{left:1033px;top:2235px;width:40px;height:150px;background:#fff;display:flex;align-items:center;justify-content:center}
.tab span{writing-mode:vertical-rl;transform:rotate(180deg);font:700 13px "Ubuntu",sans-serif;color:#222;text-decoration:underline}
.feat{position:absolute;left:650px;display:flex;gap:26px;align-items:flex-start}
.feat .ic{width:68px;height:68px;border:2px solid #fff;border-radius:50%;flex:none;display:flex;align-items:center;justify-content:center}
.feat h4{color:#fff;font-size:17px;margin-top:4px}
.feat p{color:#fff;font-size:12px;line-height:21px;width:250px;margin-top:4px}

/* gallery */
.g-img{position:absolute}
.play{left:556px;top:3056px;width:76px;height:76px;border-radius:50%;background:#4ec79a;display:flex;align-items:center;justify-content:center}

/* quote */
.q-red{left:0;top:3354px;width:455px;height:584px;background:linear-gradient(180deg,#b52a35,#c9414b)}
.q-dark{left:455px;top:3354px;width:745px;height:584px;background:#262626}
.q-vert{left:48px;top:3478px;width:50px;height:340px;display:flex;align-items:center;justify-content:center}
.q-vert span{writing-mode:vertical-rl;transform:rotate(180deg);font:700 36px "Ubuntu",sans-serif;color:#fff;letter-spacing:1px;white-space:nowrap}
.field{position:absolute;border:2px solid #555;border-radius:3px;color:#999;font-size:9px;padding:10px 14px}
.q h2{left:630px;top:3472px;font-size:34px;color:#fff;font-weight:700}
.hr{position:absolute;height:1px;background:#777}

/* testimonials */
.t-card{left:487px;top:4147px;width:449px;height:288px;background:#fff;box-shadow:0 6px 24px rgba(0,0,0,.1);padding:42px 44px}
.t-card p{font-size:12px;line-height:22px;color:#777;margin-top:14px}
.t-card h4{font-size:17px;color:#222;margin-top:24px}
.arrow-c{position:absolute;display:flex;align-items:center;justify-content:center}

/* footer */
.footer{left:0;top:4540px;width:1200px;height:581px;background:var(--navy);color:#fff}
.f-col h4{font-size:20px;font-weight:700}
.f-col h4::after{content:"";display:block;width:44px;height:3px;background:var(--red);margin-top:8px}
.links{display:grid;grid-template-columns:160px 140px;row-gap:10px;font-size:13px;margin-top:38px}
.links span::before{content:"›";margin-right:14px}
.contact-bar{left:85px;top:4973px;width:1026px;height:84px;background:var(--navy-2);border-radius:4px;display:flex}
.cb-item{flex:1;display:flex;align-items:center;gap:20px;padding-left:30px;font-size:14px;border-right:1px solid #3a4258}
.cb-item:last-child{border:0}
.cb-item b{display:block;font-size:14px}
</style>
</head>
<body>

<!-- HERO -->
<section class="hero">
  <div class="ph hero-photo" role="img" aria-label="Photo of two business professionals reviewing a tablet in a modern office"></div>
  <div class="ph hero-shade"></div>
  <div class="abs hero-rule"></div>
  <div class="abs logo" style="left:100px;top:32px">Lucent Prose Advisory Group</div>
  <nav class="abs nav"><span class="active">HOME</span><span>ABOUT</span><span>SERVICES</span><span>CASES</span><span>BLOG</span><span>CONTACT+-</span></nav>
  <div class="abs phone">
    <svg width="18" height="18" viewBox="0 0 24 24" fill="none" stroke="#fff" stroke-width="2"><path d="M5 3h4l2 5-3 2a11 11 0 0 0 6 6l2-3 5 2v4a2 2 0 0 1-2 2A17 17 0 0 1 3 5a2 2 0 0 1 2-2z"/></svg>
    <div><small>Have Any Questions?</small><b>+61 3 5550 1042</b></div>
  </div>
  <div class="abs social" style="top:268px"></div>
  <div class="abs social" style="top:312px"></div>
  <div class="abs social" style="top:354px;background:var(--teal);border-color:var(--teal)"></div>
  <div class="abs social" style="top:394px"></div>
  <h1 class="abs">Words That Speak,<br>Strategies That Succeed</h1>
  <p class="abs">Lorem ipsum dolor sit amet, consectetur adipiscing elit, sed do eiusmod tempor incididunt ut labore et dolore magna aliqua.</p>
  <div class="btn" style="left:234px;top:403px;width:150px;height:40px">Read More <svg viewBox="0 0 16 12" fill="none" stroke="#fff" stroke-width="1.6"><path d="M1 6h13M9 1l5 5-5 5"/></svg></div>
  <svg class="abs" style="left:0;top:600px" width="1200" height="76" viewBox="0 0 1200 76"><path d="M398 76 C430 20 440 8 500 8 L1200 8 L1200 76 Z" fill="#fff"/></svg>
</section>

<!-- ABOUT -->
<section class="about">
  <div class="abs label" style="left:117px;top:820px">About Us</div>
  <h2 class="abs">Every Word Counts,<br>Every Message Matters</h2>
  <p class="abs">Lorem ipsum dolor sit amet, consectetur adipiscing elit, sed do eiusmod tempor incididunt ut labore et dolore magna aliqua. Ut enim ad minim veniam, q</p>
  <div class="abs quote-line">"Writing Excellence, Pioneering Impact"</div>
  <div class="ph" style="left:572px;top:791px;width:523px;height:401px;background:linear-gradient(120deg,#8f9aa5,#c8d0d6 50%,#5d6b7a)" role="img" aria-label="Photo of a consultant in a sweater holding a tablet"></div>
  <div class="abs" style="left:1120px;top:791px;width:3px;height:104px;background:var(--teal)"></div>
  <div class="abs" style="left:815px;top:1207px;width:280px;height:3px;background:linear-gradient(90deg,var(--teal),rgba(61,191,216,0))"></div>
  <div class="ph" style="left:121px;top:1099px;width:324px;height:220px;background:linear-gradient(120deg,#b8c0c8,#e6e9ec 55%,#7e8894)" role="img" aria-label="Photo of a professional woman holding a notebook"></div>
  <div class="ph" style="left:475px;top:1099px;width:326px;height:220px;background:linear-gradient(120deg,#5d6877,#aab4be 55%,#3f4955)" role="img" aria-label="Photo of two colleagues working at a laptop"></div>
</section>

<!-- SERVICES -->
<section class="abs services"></section>
<div class="sec-title" style="top:1470px"><span class="label">Our Latest Services</span><h2>Services We Provide</h2></div>

<div class="ph" style="left:93px;top:1596px;width:320px;height:399px;background:linear-gradient(140deg,#6b7886,#b9c2ca 60%,#4d5866)" role="img" aria-label="Photo of two women discussing strategy"></div>
<div class="card-box" style="left:121px;top:1810px;width:264px;height:226px"><h3>Communication<br>Strategy</h3><p>Lorem ipsum dolor sit amet, ae consectetur adipiscing</p><div class="go"><svg width="12" height="12" viewBox="0 0 12 12" fill="none" stroke="#fff" stroke-width="2"><path d="M4 1l5 5-5 5"/></svg></div></div>

<div class="ph" style="left:439px;top:1635px;width:320px;height:401px;background:linear-gradient(140deg,#405066,#8898aa 60%,#2f3b4d)" role="img" aria-label="Photo of a man holding a tablet"></div>
<div class="card-box" style="left:467px;top:1596px;width:264px;height:224px"><h3>Technical<br>Writing</h3><p>Lorem ipsum dolor sit amet, ae consectetur adipiscing</p><div class="go"><svg width="12" height="12" viewBox="0 0 12 12" fill="none" stroke="#fff" stroke-width="2"><path d="M4 1l5 5-5 5"/></svg></div></div>

<div class="ph" style="left:787px;top:1596px;width:320px;height:399px;background:linear-gradient(140deg,#8c7a6e,#c8bdb4 55%,#6a5a50)" role="img" aria-label="Photo of a team laughing together around a table"></div>
<div class="card-box" style="left:815px;top:1810px;width:264px;height:226px"><h3>Content<br>Creation</h3><p>Lorem ipsum dolor sit amet, ae consectetur adipiscing</p><div class="go"><svg width="12" height="12" viewBox="0 0 12 12" fill="none" stroke="#fff" stroke-width="2"><path d="M4 1l5 5-5 5"/></svg></div></div>

<!-- WHY -->
<section class="why">
  <div class="ph why-red" role="img" aria-label="Red-tinted photo of a business meeting"></div>
  <div class="abs why-black"></div>
  <div class="abs label" style="left:117px;top:2278px">Why we are the Best</div>
  <h2 class="abs">Eloquent Expression,<br>Profound Impression.</h2>
  <p class="abs">Lorem ipsum dolor sit amet, consectetur adipiscing elit, sed do eiusmod tempor incididunt ut labore et dolore magna aliqua. Ut enim ad minim veniam, q</p>
  <div class="btn" style="left:127px;top:2530px;width:151px;height:41px">Read More <svg viewBox="0 0 16 12" fill="none" stroke="#fff" stroke-width="1.6"><path d="M1 6h13M9 1l5 5-5 5"/></svg></div>
  <div class="abs why-frame"></div>
  <div class="abs tab"><span>GET A QUOTE</span></div>
  <div class="feat" style="top:2272px"><div class="ic"><svg width="30" height="30" viewBox="0 0 24 24" fill="none" stroke="#fff" stroke-width="1.5"><circle cx="12" cy="8" r="4"/><path d="M4 21c1-5 4-7 8-7s7 2 8 7"/></svg></div><div><h4>Empathetic Staff</h4><p>Lorem ipsum dolor sit amet, consecte tur adipiscing elit, sed do</p></div></div>
  <div class="feat" style="top:2385px"><div class="ic"><svg width="30" height="30" viewBox="0 0 24 24" fill="none" stroke="#fff" stroke-width="1.5"><path d="M12 3l2.6 5.4 5.9.8-4.3 4.1 1 5.8L12 16.3 6.8 19.1l1-5.8L3.5 9.2l5.9-.8z"/></svg></div><div><h4>Client-Centric</h4><p>Lorem ipsum dolor sit amet, consecte tur adipiscing elit, sed do</p></div></div>
  <div class="feat" style="top:2496px"><div class="ic"><svg width="30" height="30" viewBox="0 0 24 24" fill="none" stroke="#fff" stroke-width="1.5"><path d="M4 17a8 8 0 1 1 16 0"/><path d="M12 17l3-6"/><circle cx="12" cy="17" r="1.5"/></svg></div><div><h4>Professionalism</h4><p>Lorem ipsum dolor sit amet, consecte tur adipiscing elit, sed do</p></div></div>
</section>

<!-- GALLERY -->
<div class="sec-title" style="top:2782px"><span class="label">Gallery</span><h2>Our Gallery</h2></div>
<div class="g-img" style="left:93px;top:2905px;width:233px;height:374px;clip-path:polygon(0 12%,100% 0,100% 100%,0 88%);background:linear-gradient(130deg,#c9d3dc,#e9edf0 50%,#9fb0c0)" role="img" aria-label="Photo of a woman reading a document"></div>
<div class="g-img" style="left:354px;top:2905px;width:494px;height:374px;background:linear-gradient(130deg,#5f6c78,#b7c2cb 55%,#3d4a57)" role="img" aria-label="Photo of two businessmen looking at a tablet"></div>
<div class="abs play"><svg width="30" height="34" viewBox="0 0 30 34"><path d="M4 2l24 15-24 15z" fill="#fff"/></svg></div>
<div class="g-img" style="left:874px;top:2905px;width:233px;height:374px;clip-path:polygon(0 0,100% 12%,100% 88%,0 100%);background:linear-gradient(130deg,#b4bcc4,#e2e5e8 50%,#8e98a2)" role="img" aria-label="Photo of a busy open-plan office"></div>

<!-- QUOTE -->
<section class="q">
  <div class="abs q-red"></div>
  <div class="abs q-dark"></div>
  <div class="ph" style="left:118px;top:3400px;width:480px;height:538px;background:linear-gradient(180deg,rgba(60,60,70,0),rgba(40,40,50,.85) 30%,#2b2b33);border-radius:200px 200px 0 0" role="img" aria-label="Photo of a smiling businessman and businesswoman standing back to back"></div>
  <div class="abs q-vert"><span>GET A FREE QUOTE</span></div>
  <div class="hr" style="left:455px;top:3452px;width:122px"></div>
  <div class="hr" style="left:904px;top:3452px;width:296px"></div>
  <div class="abs label" style="left:630px;top:3431px">Contact Us</div>
  <h2 class="abs">GET A FREE QUOTE</h2>
  <div class="field" style="left:634px;top:3539px;width:202px;height:32px">Your Name</div>
  <div class="field" style="left:864px;top:3539px;width:207px;height:32px">Phone Number</div>
  <div class="field" style="left:634px;top:3597px;width:202px;height:33px">Email Address</div>
  <div class="field" style="left:864px;top:3597px;width:207px;height:33px">Location</div>
  <div class="field" style="left:634px;top:3656px;width:437px;height:131px">Your Message</div>
  <div class="hr" style="left:0;top:3839px;width:583px"></div>
  <div class="hr" style="left:815px;top:3839px;width:385px"></div>
  <div class="btn" style="left:626px;top:3821px;width:151px;height:42px">Read More <svg viewBox="0 0 16 12" fill="none" stroke="#fff" stroke-width="1.6"><path d="M1 6h13M9 1l5 5-5 5"/></svg></div>
</section>

<!-- TESTIMONIALS -->
<div class="sec-title" style="top:4037px"><span class="label">Our Testimonials</span><h2>Client Reviews</h2></div>
<div class="ph" style="left:99px;top:4147px;width:135px;height:288px;background:linear-gradient(160deg,#4a4e58,#7d8390)" role="img" aria-label="Portrait photo of a client"></div>
<div class="arrow-c" style="left:140px;top:4275px"><svg width="32" height="32" viewBox="0 0 24 24" fill="none" stroke="#fff" stroke-width="2"><path d="M20 12H5M11 6l-6 6 6 6"/></svg></div>
<div class="ph" style="left:260px;top:4147px;width:227px;height:288px;background:linear-gradient(160deg,#8a8f96,#c8cbd0 60%,#6e737a)" role="img" aria-label="Portrait photo of a smiling client with glasses"></div>
<div class="abs t-card">
  <svg width="34" height="24" viewBox="0 0 34 24" fill="#1e2a5a"><path d="M0 24V12C0 5 4 1 11 0v5c-3 1-5 3-5 7h5v12zM18 24V12c0-7 4-11 11-12v5c-3 1-5 3-5 7h5v12z"/></svg>
  <p>Lorem ipsum dolor sit amet, consectetur adipiscing elit, sed do eiusmod tempor incididunt ut labore et dolore magna aliqua. Ut enim ad minim veniam, qcididunt ut labore et dolore magna aliqua.</p>
  <h4>Clara Whitfield</h4>
  <div style="display:flex;justify-content:space-between;font-size:10px;color:#999"><span>Chairperson</span><span style="color:#e8731a;font-size:13px;margin-top:-22px">★★★★★</span></div>
</div>
<div class="ph" style="left:962px;top:4147px;width:137px;height:288px;background:linear-gradient(160deg,#3f3a38,#7a6b62)" role="img" aria-label="Portrait photo of a client"></div>
<div class="arrow-c" style="left:1020px;top:4275px"><svg width="32" height="32" viewBox="0 0 24 24" fill="none" stroke="#fff" stroke-width="2"><path d="M4 12h15M13 6l6 6-6 6"/></svg></div>

<!-- FOOTER -->
<footer class="abs footer">
  <div class="abs logo" style="left:95px;top:100px;font-size:16px">Lucent Prose Advisory Group</div>
  <div class="abs" style="left:83px;top:168px;font-size:18px;font-weight:700">800-555-0182</div>
  <div class="abs" style="left:85px;top:195px;font-size:12px;font-weight:700">Call for free consultation</div>
  <div class="abs" style="left:85px;top:230px;width:270px;font-size:12px;line-height:22px;color:#d5d8e0">Lorem ipsum dolor sit amet, consectet sed do eiusmod tempor incididunt ut la magna aliqua. Ut enim</div>
  <div class="abs" style="left:85px;top:314px;font-size:13px;font-weight:700">Read more ›</div>

  <div class="abs f-col" style="left:437px;top:92px">
    <h4>Useful Links</h4>
    <div class="links"><span>About Company</span><span>Services</span><span>Leadership</span><span>Industries</span><span>Blog Post</span><span>Feedback</span><span>FAQ'S</span><span>Partners</span><span>Certification</span><span>Pricing</span><span>Testimonials</span><span>Contct</span></div>
  </div>

  <div class="abs f-col" style="left:789px;top:92px">
    <h4>Newsletter</h4>
    <p style="font-size:12px;line-height:24px;width:320px;margin-top:38px;font-weight:600">Dont miss to subscribe to our news feeds. kindly fill the form below</p>
    <div style="display:flex;margin-top:20px;width:318px;height:48px;background:var(--navy-2);border-radius:24px;align-items:center;justify-content:space-between;padding-left:22px">
      <span style="font-size:12px;font-weight:600">Your Email Address</span>
      <span style="width:52px;height:48px;background:var(--red);border-radius:0 24px 24px 0;display:flex;align-items:center;justify-content:center"><svg width="14" height="14" viewBox="0 0 12 12" fill="none" stroke="#fff" stroke-width="2"><path d="M4 1l5 5-5 5"/></svg></span>
    </div>
  </div>
</footer>

<div class="abs contact-bar" style="color:#fff">
  <div class="cb-item"><svg width="28" height="32" viewBox="0 0 24 28" fill="none" stroke="#d43b45" stroke-width="1.8"><path d="M12 27s9-9 9-16a9 9 0 0 0-18 0c0 7 9 16 9 16z"/><circle cx="12" cy="11" r="3.5"/></svg><div><b>Location</b>246 Rd, Country</div></div>
  <div class="cb-item"><svg width="30" height="28" viewBox="0 0 26 24" fill="none" stroke="#d43b45" stroke-width="1.8"><rect x="2" y="2" width="22" height="16" rx="2"/><path d="M6 18v5l5-5M7 8h12M7 12h8"/></svg><div><b>Mail us</b>hello@lucentprose.example</div></div>
  <div class="cb-item"><svg width="30" height="28" viewBox="0 0 24 24" fill="none" stroke="#d43b45" stroke-width="1.8"><path d="M22 2L2 10l8 3 3 8z"/><path d="M22 2L10 13"/></svg><div><b>Office hrs</b>9.00am to 7.00pm (Mon-Sat)</div></div>
</div>
<div class="abs" style="left:1125px;top:5027px;width:47px;height:46px;background:var(--red);border-radius:3px;display:flex;align-items:center;justify-content:center"><svg width="18" height="12" viewBox="0 0 18 12" fill="none" stroke="#fff" stroke-width="2.4"><path d="M2 10l7-7 7 7"/></svg></div>
<div class="abs" style="left:85px;top:5080px;font-size:12px;color:#333">Lucent Prose Advisory Group</div>
<div class="abs" style="left:800px;top:5080px;font-size:12px;color:#333;display:flex;gap:24px"><span>Privacy Policy</span><span>Terms &amp; Conditions</span><span>Site Map</span></div>

</body>
</html>
```